Poster Design Project

We are a non-profit organization that organizes various social events for Indian senior citizens to promote a healthy lifestyle, share knowledge & companionship among them.

One such event that we are organizing for them is, "Lanterns and Footwork Gala" - (On the lines of Steps Under Lanterns), with the seniors as our stars.

We need a poster design for this event that incorporates the Steps Under Lanterns theme as well as some Indian Cinema (Bollywood) themes. We are open to different color schemes and design concepts.

The poster design should include the event location, time, ticket prices, contact information (up to 3 contacts), and a small note (i.e. "Snacks will be available for purchase."). We are also looking for a flyer design which would be similar to the poster.

We have uploaded our Sahyog Seniors for your reference.

Indian Community (Families and Senior Citizens)

Non-Profit

• Focused on seniors as our stars
Should look professional
• It would be great if an event based logo could be put on the poster and flyer, which would be based on/integrated with the Sahyog Seniors. The concept used in files 2 and 9 could be combined with the Sahyog Seniors (file 6) to form the event logo.

Some ideas we thought of were movie posters, "Steps Under Lanterns", "Kadam Milao Re" or similar shows' concepts, etc.

We have attached some more images as examples of some indian dance movie posters.
• It's a family event so

```html
<!DOCTYPE html>
<html lang="en">
<head>
<meta charset="utf-8">
<title>Lanterns and Footwork Gala</title>
<link rel="stylesheet" href="https://fonts.googleapis.com/css2?family=Great+Vibes&family=Arimo:wght@700&display=swap">
<style>
  :root {
    --teal-deep: #0a4148;
    --teal-mid: #136a72;
    --teal-light: #23838b;
    --ink-white: #ffffff;
    --photo-cream: #f3ecd9;
    --photo-cream-shade: #d9ccad;
    --photo-gold: #eeaa1e;
    --photo-gold-deep: #c9820f;
    --badge-red: #c8242c;
  }
  * { margin: 0; padding: 0; box-sizing: border-box; }
  html, body { width: 1200px; height: 605px; overflow: hidden; }
  body { background: var(--teal-deep); }
  .poster {
    position: relative;
    width: 1200px;
    height: 605px;
    overflow: hidden;
    background: radial-gradient(ellipse at 50% 45%, var(--teal-light) 0%, var(--teal-mid) 50%, var(--teal-deep) 100%);
    color: var(--ink-white);
    font-family: "Arimo", Arial, sans-serif;
    font-weight: 700;
  }
  .org-mark {
    position: absolute;
    left: 330px;
    top: 72px;
    display: flex;
    align-items: center;
    gap: 10px;
  }
  .org-mark__square {
    width: 22px;
    height: 22px;
    background: var(--badge-red);
  }
  .org-mark__name {
    font-size: 20px;
    color: var(--ink-white);
    letter-spacing: 1px;
  }
  .event-title {
    position: absolute;
    left: 62px;
    top: 128px;
    font-family: "Great Vibes", cursive;
    font-weight: 400;
    line-height: 1;
    text-shadow: 0 2px 4px rgba(0,0,0,0.35);
  }
  .event-title__big { display: block; font-size: 112px; }
  .event-title__small { display: block; font-size: 50px; margin: -10px 0 -6px 80px; }
  .event-title__big--last { margin-left: 130px; }
  .event-details {
    position: absolute;
    left: 82px;
    top: 424px;
    font-size: 18px;
    line-height: 27px;
  }
  .contact {
    position: absolute;
    left: 323px;
    top: 424px;
    font-size: 18px;
    line-height: 27px;
  }
  .contact__numbers {
    list-style: none;
    margin: 9px 0 0 84px;
    line-height: 26px;
  }
  .note {
    position: absolute;
    left: 82px;
    top: 562px;
    font-size: 16px;
  }
  .dancers-photo {
    position: absolute;
    left: 560px;
    top: 40px;
    width: 640px;
    height: 565px;
  }
</style>
</head>
<body>
  <main class="poster">
    <div class="org-mark">
      <span class="org-mark__square"></span>
      <span class="org-mark__name">Sahyog Seniors</span>
    </div>

    <h1 class="event-title">
      <span class="event-title__big">Lanterns</span>
      <span class="event-title__small">and Footwork</span>
      <span class="event-title__big event-title__big--last">Gala</span>
    </h1>

    <div class="event-details">
      <p>Location : India</p>
      <p>Time : 7pm to 12 am</p>
      <p>Ticket Prices : INR 300</p>
    </div>

    <div class="contact">
      <p>Contact Information :</p>
      <ul class="contact__numbers">
        <li>98210-40561</li>
        <li>98210-40562</li>
        <li>98210-40563</li>
      </ul>
    </div>

    <p class="note">Note: Snacks will be available for purchase</p>

    <svg class="dancers-photo" role="img" aria-label="Photograph of a senior Bollywood dancing couple: a man in a cream sherwani and a woman in a golden yellow saree, posed mid-step" viewBox="0 0 640 565" xmlns="http://www.w3.org/2000/svg">
      <defs>
        <radialGradient id="tone-cream" cx="0.5" cy="0.55" r="0.5">
          <stop offset="0" stop-color="var(--photo-cream)"/>
          <stop offset="0.6" stop-color="var(--photo-cream-shade)" stop-opacity="0.9"/>
          <stop offset="1" stop-color="var(--photo-cream-shade)" stop-opacity="0"/>
        </radialGradient>
        <radialGradient id="tone-gold" cx="0.5" cy="0.6" r="0.5">
          <stop offset="0" stop-color="var(--photo-gold)"/>
          <stop offset="0.65" stop-color="var(--photo-gold-deep)" stop-opacity="0.85"/>
          <stop offset="1" stop-color="var(--photo-gold-deep)" stop-opacity="0"/>
        </radialGradient>
      </defs>
      <ellipse cx="430" cy="360" rx="170" ry="300" fill="url(#tone-gold)"/>
      <ellipse cx="230" cy="330" rx="210" ry="330" fill="url(#tone-cream)"/>
    </svg>
  </main>
</body>
</html>
```